Kestrel Fitness Studio Retail Tube Design

We require a design for cardboard tubes, like images included, which will be the main packaging for the clothing sold in our fitness studio. Kestrel Fitness Studio is an upscale customer service driven fitness studio that is geared towards improving our clients/members quality of life by marrying cutting edge technology like 3D scanning and metabolic measurement with first class training based on 30+ years of experience in the industry.

The project will require a design which revolves around the tube seamlessly including the lid and its top and must include the company logo, which is included, along with our web address (www.kestrelgymhall.example).

The final design should be a bold, sleek design which stands out so when people see the tube they will either know it’s from our studio or be curious as to want company it’s from. Similar to the impact the Moravanti bag has that is given to all their customers.

Target Market(s)

Individuals and groups seeking individualize fitness programs which produce results.

Industry/Entity Type

Clothing

Colors

Designer to choose colors to be used in the design.

Requirements
Must have
• Logo and website address

```html
<!DOCTYPE html>
<html lang="en">
<head>
<meta charset="utf-8">
<title>Kestrel Fitness Studio – Retail Tube Wrap</title>
<link rel="stylesheet" href="https://fonts.googleapis.com/css2?family=Josefin+Sans:wght@400;700&family=Oswald:wght@700&display=swap">
<style>
  :root {
    --stage: #e9ecee;
    --ink: #050505;
    --type: #ffffff;
    --accent: #d8303a;
    --band-light: #f4f5f6;
    --band-mid: #c9cdd1;
    --band-dark: #9ea4aa;
    --band-type: #2a2c2e;
    --runner-tone: #151515;
  }
  html, body {
    margin: 0;
    width: 1200px;
    height: 923px;
    overflow: hidden;
    background: var(--stage);
  }
  .tube-wrap {
    position: absolute;
    left: 0;
    top: 110px;
    width: 1200px;
    height: 704px;
    display: block;
  }
  .word { fill: var(--type); font-family: "Josefin Sans", sans-serif; font-weight: 400; }
  .word--bold { font-weight: 700; }
  .word--condensed { font-family: "Oswald", sans-serif; font-weight: 700; }
  .band-name, .band-url { fill: var(--band-type); font-family: "Josefin Sans", sans-serif; font-weight: 400; }
  .accent-block { fill: var(--accent); }
</style>
</head>
<body>
<svg class="tube-wrap" viewBox="0 0 1037 608" xmlns="http://www.w3.org/2000/svg">
  <defs>
    <clipPath id="panel-clip"><rect x="0" y="0" width="1037" height="608"/></clipPath>
    <linearGradient id="band-sheen" x1="0" y1="0" x2="0" y2="1">
      <stop offset="0" stop-color="var(--band-dark)"/>
      <stop offset="0.35" stop-color="var(--band-light)"/>
      <stop offset="0.75" stop-color="var(--band-mid)"/>
      <stop offset="1" stop-color="var(--band-dark)"/>
    </linearGradient>
    <radialGradient id="runner-glow" cx="0.55" cy="0.5" r="0.6">
      <stop offset="0" stop-color="var(--runner-tone)"/>
      <stop offset="1" stop-color="var(--ink)"/>
    </radialGradient>
  </defs>

  <g clip-path="url(#panel-clip)">
    <rect class="panel-ground" x="0" y="0" width="1037" height="523" fill="var(--ink)"/>
    <rect class="runner-art" x="40" y="0" width="980" height="523" fill="url(#runner-glow)"
          role="img" aria-label="White line drawing of three runners in motion with speed streaks"/>

    <g class="word-cloud">
      <text class="word" x="13" y="43" font-size="38" textLength="607" lengthAdjust="spacingAndGlyphs">FITNESS.FRAMEWORK.FUNCTION</text>
      <text class="word word--bold" x="652" y="47" font-size="52" textLength="295" lengthAdjust="spacingAndGlyphs">ISOKINETIC</text>
      <text class="word word--bold" x="652" y="97" font-size="52" textLength="295" lengthAdjust="spacingAndGlyphs">EXERCISE</text>
      <text class="word word--condensed" x="25" y="98" font-size="34" textLength="250" lengthAdjust="spacingAndGlyphs">CARDIORESPIRATORY</text>
      <text class="word word--bold" x="38" y="145" font-size="40" textLength="215" lengthAdjust="spacing">FITNESS</text>
      <text class="word" x="288" y="96" font-size="46" textLength="330" lengthAdjust="spacingAndGlyphs">CUTTING EDGE</text>
      <text class="word" x="288" y="145" font-size="46" textLength="330" lengthAdjust="spacingAndGlyphs">TECHNOLOGY</text>
      <text class="word" x="652" y="138" font-size="28" textLength="370" lengthAdjust="spacingAndGlyphs">CARDIOVASCULAR SYSTEM</text>
      <text class="word" x="15" y="213" font-size="46" textLength="225" lengthAdjust="spacingAndGlyphs">3D SCAN</text>
      <text class="word" x="15" y="262" font-size="46" textLength="230" lengthAdjust="spacing">YOUR</text>
      <text class="word" x="15" y="312" font-size="46" textLength="230" lengthAdjust="spacing">BODY</text>
      <text class="word" x="262" y="200" font-size="58" textLength="655" lengthAdjust="spacingAndGlyphs">FIRST CLASS TRAINING</text>
      <text class="word word--bold" x="340" y="280" font-size="82" textLength="160" lengthAdjust="spacingAndGlyphs">BMI</text>
      <text class="word word--bold" x="588" y="280" font-size="82" textLength="275" lengthAdjust="spacingAndGlyphs">ACTIVE</text>
      <text class="word" x="283" y="315" font-size="28" textLength="272" lengthAdjust="spacingAndGlyphs">BODY MASS INDEX</text>
      <text class="word word--bold" x="588" y="350" font-size="82" textLength="285" lengthAdjust="spacingAndGlyphs">ABILITY</text>
      <text class="word" x="13" y="360" font-size="44" textLength="565" lengthAdjust="spacingAndGlyphs">METABOLIC MEASUREMENT</text>
      <text class="word" x="475" y="398" font-size="40" textLength="600" lengthAdjust="spacingAndGlyphs">CONCENTRIC MUSCLE ACTION</text>
      <text class="word word--bold" x="180" y="412" font-size="52" textLength="265" lengthAdjust="spacingAndGlyphs">MAXIMIZE</text>
      <text class="word word--bold" x="180" y="463" font-size="52" textLength="250" lengthAdjust="spacingAndGlyphs">MEASURE</text>
      <text class="word word--bold" x="180" y="515" font-size="52" textLength="255" lengthAdjust="spacingAndGlyphs">MOTIVATE</text>
      <text class="word" x="450" y="437" font-size="30" textLength="135" lengthAdjust="spacing">TARGET</text>
      <text class="word" x="450" y="473" font-size="30" textLength="135" lengthAdjust="spacingAndGlyphs">MUSCLES</text>
      <text class="word" x="450" y="506" font-size="30" textLength="135" lengthAdjust="spacing">TRAIN</text>
      <text class="word word--bold" x="718" y="437" font-size="44" textLength="345" lengthAdjust="spacingAndGlyphs">HEART RATE</text>
      <text class="word word--bold" x="718" y="483" font-size="44" textLength="360" lengthAdjust="spacing">RESERVE</text>
      <text class="word" x="718" y="517" font-size="34" textLength="350" lengthAdjust="spacingAndGlyphs">BREATHE.BALANCE</text>
    </g>

    <rect class="accent-block" x="70" y="428" width="80" height="80"/>
    <rect class="accent-block" x="612" y="428" width="80" height="80"/>

    <rect class="brand-band" x="0" y="523" width="1037" height="85" fill="url(#band-sheen)"/>
    <text class="band-name" x="10" y="575" font-size="24" textLength="235" lengthAdjust="spacingAndGlyphs">KESTREL FITNESS STUDIO</text>
    <text class="band-url" x="262" y="574" font-size="19" textLength="260" lengthAdjust="spacingAndGlyphs">www.kestrelgymhall.example</text>
    <text class="band-name" x="545" y="575" font-size="24" textLength="235" lengthAdjust="spacingAndGlyphs">KESTREL FITNESS STUDIO</text>
    <text class="band-url" x="800" y="574" font-size="19" textLength="260" lengthAdjust="spacingAndGlyphs">www.kestrelgymhall.example</text>
  </g>
</svg>
</body>
</html>
```